Business Card Design Project

I want a design for my business cards based on an excisting logo design.

Target Market(s)

Marketeers, PR-peeps, CEO's, decisionmakers, entrepreneurs

Industry/Entity Type

Business

Requirements
Nice to have
• Some visual interest on the back too
Should not have
• Sarif on the font

```html
<!DOCTYPE html>
<html lang="en">
<head>
<meta charset="utf-8">
<title>SproutPR business card</title>
<link rel="stylesheet" href="https://fonts.googleapis.com/css2?family=Cabin:wght@400;600;700&display=swap">
<style>
  :root {
    --stage: #161616;
    --leaf: #84b11c;
    --paper: #f4f4f1;
    --ink: #333333;
    --wordmark: #555555;
    --deep-green: #1c7b2a;
    --label: #ffffff;
  }
  * { margin: 0; padding: 0; box-sizing: border-box; }
  html, body {
    width: 1200px;
    height: 800px;
    overflow: hidden;
    background: var(--stage);
    font-family: "Cabin", sans-serif;
  }
  .canvas { position: relative; width: 1200px; height: 800px; }
  .side-label {
    position: absolute;
    top: 92px;
    width: 297px;
    text-align: center;
    color: var(--label);
    font-size: 26px;
    font-weight: 400;
  }
  .card {
    position: absolute;
    top: 140px;
    width: 297px;
    height: 521px;
    overflow: hidden;
  }
  .card-back {
    left: 279px;
    background: var(--leaf);
    border-radius: 43px 13px 13px 13px;
  }
  .card-front {
    left: 623px;
    background: var(--leaf);
    border-radius: 13px 43px 13px 13px;
  }
  .front-field { position: absolute; inset: 0; }
  .brand-dot {
    position: absolute;
    border-radius: 50%;
  }
  .card-back .brand-dot {
    left: 85px; top: 178px; width: 124px; height: 124px;
    background: var(--paper);
  }
  .card-front .brand-dot {
    left: 95px; top: 86px; width: 110px; height: 110px;
    background: var(--leaf);
  }
  .brand-name {
    position: absolute;
    left: 0; right: 0;
    text-align: center;
    color: var(--wordmark);
    font-weight: 400;
    letter-spacing: 2px;
  }
  .card-back .brand-name { top: 320px; font-size: 30px; }
  .card-front .brand-name { top: 204px; font-size: 26px; }
  .website {
    position: absolute;
    left: 0; right: 0; top: 412px;
    text-align: center;
    color: var(--deep-green);
    font-size: 17px;
  }
  .person-name {
    position: absolute; left: 0; right: 0; top: 280px;
    text-align: center; color: var(--ink);
    font-size: 17px; font-weight: 700;
  }
  .contact {
    position: absolute; left: 0; right: 0; top: 334px;
    text-align: center; color: var(--ink);
    font-size: 15px; line-height: 23px;
  }
  .address {
    position: absolute; left: 0; right: 0; top: 448px;
    text-align: center; color: var(--paper);
    font-size: 13px;
  }
  .socials {
    position: absolute; left: 0; right: 0; top: 476px;
    display: flex; justify-content: center; gap: 38px;
    color: var(--deep-green); font-size: 13px;
  }
  .social { display: flex; align-items: center; gap: 4px; }
  .social-mark {
    width: 10px; height: 10px; border-radius: 2px;
    background: var(--deep-green);
  }
</style>
</head>
<body>
<div class="canvas">
  <div class="side-label" style="left:279px">Back</div>
  <div class="side-label" style="left:623px">Front</div>

  <section class="card card-back">
    <div class="brand-dot"></div>
    <div class="brand-name">SproutPR</div>
    <div class="website">www.sproutpr.nl</div>
  </section>

  <section class="card card-front">
    <svg class="front-field" width="297" height="521" viewBox="0 0 297 521" aria-hidden="true">
      <path d="M122 0 Q40 25 0 79 L0 379 Q60 445 152 438 Q252 430 297 353 L297 0 Z" fill="var(--paper)"/>
    </svg>
    <div class="brand-dot"></div>
    <div class="brand-name">SproutPR</div>
    <div class="person-name">Marit Jansen</div>
    <div class="contact">marit.jansen@sproutpr.nl<br>+31(0)6 20481935</div>
    <div class="address">Lindelaan 42 6712 AB Ede</div>
    <div class="socials">
      <span class="social"><span class="social-mark"></span>_sproutpr</span>
      <span class="social"><span class="social-mark"></span>sproutpr</span>
    </div>
  </section>
</div>
</body>
</html>
```